The amber lantern with an elephant incorporated in the background

Target Market(s)

Real estate

Industry/Entity Type

Real Estate

Contact Information for Business Card

On back on want my name & number
In front I want the business name, "the amber lantern", below to say staging & design

Logo Text

The amber lantern

Font styles to use
Serif

Colors
000000

Requirements
Must have
• I want an elephant behind the writing in gold transperant

```html
<!DOCTYPE html>
<html lang="en">
<head>
<meta charset="utf-8">
<title>The Amber Lantern — Business Card</title>
<link rel="stylesheet" href="https://fonts.googleapis.com/css2?family=Lora:wght@400;600;700&display=swap">
<style>
  :root {
    --page: #ffffff;
    --card: #070707;
    --band: #ecd922;
    --ink: #0a0a0a;
    --gold-light: #f1d23a;
    --gold-deep: #c9a114;
  }
  html, body {
    margin: 0;
    padding: 0;
    width: 800px;
    height: 1200px;
    overflow: hidden;
    background: var(--page);
  }
  .canvas {
    position: relative;
    width: 800px;
    height: 1200px;
    font-family: "Lora", Georgia, serif;
    color: var(--ink);
  }
  .card {
    position: absolute;
    left: 48px;
    width: 672px;
    height: 384px;
    background: var(--card);
    overflow: hidden;
  }
  .card--front { top: 104px; }
  .card--back { top: 549px; }
  .band {
    position: absolute;
    left: 0;
    width: 100%;
    background: var(--band);
  }
  .card--front .band { top: 208px; height: 53px; }
  .card--back .band { top: 210px; height: 50px; }
  .elephant {
    position: absolute;
    background: linear-gradient(135deg, var(--gold-light), var(--gold-deep));
    opacity: 0.95;
  }
  .card--front .elephant {
    left: 0;
    top: 16px;
    width: 138px;
    height: 190px;
    border-radius: 0 60px 20px 0;
  }
  .card--back .elephant {
    right: 0;
    top: 19px;
    width: 182px;
    height: 180px;
    border-radius: 70px 0 20px 30px;
  }
  .brand {
    position: absolute;
    margin: 0;
    padding: 0;
    left: 260px;
    width: 392px;
    top: 208px;
    height: 53px;
    display: flex;
    flex-direction: column;
    justify-content: center;
    align-items: center;
    font-weight: 400;
    text-align: center;
  }
  .brand__name {
    display: block;
    font-size: 29px;
    line-height: 27px;
    font-weight: 400;
  }
  .brand__tagline {
    display: block;
    font-size: 23px;
    line-height: 22px;
    font-weight: 400;
  }
  .contact {
    position: absolute;
    left: 37px;
    top: 210px;
    height: 50px;
    display: flex;
    align-items: center;
  }
  .contact__name {
    font-size: 33px;
    font-weight: 400;
  }
  .contact__divider {
    width: 3px;
    height: 38px;
    background: var(--ink);
    margin: 0 24px 0 26px;
  }
  .contact__phone {
    display: flex;
    align-items: center;
    font-size: 22px;
    font-weight: 700;
  }
  .contact__phone svg { margin-right: 6px; }
</style>
</head>
<body>
<main class="canvas">
  <section class="card card--front">
    <div class="elephant" role="img" aria-label="Gold textured elephant silhouette walking in from the left"></div>
    <div class="band"></div>
    <h1 class="brand">
      <span class="brand__name">The Amber Lantern</span>
      <span class="brand__tagline">staging &amp; design</span>
    </h1>
  </section>

  <section class="card card--back">
    <div class="elephant" role="img" aria-label="Gold textured elephant silhouette walking in from the right"></div>
    <div class="band"></div>
    <div class="contact">
      <span class="contact__name">Mara Quill</span>
      <span class="contact__divider"></span>
      <span class="contact__phone">
        <svg width="24" height="24" viewBox="0 0 24 24" aria-hidden="true">
          <path fill="#0a0a0a" d="M6.6 10.8c1.4 2.8 3.8 5.1 6.6 6.6l2.2-2.2c.3-.3.7-.4 1-.2 1.1.4 2.300.6 3.6.6.6 0 1 .4 1 1V20c0 .6-.4 1-1 1C10.6 21 3 13.4 3 4c0-.6.4-1 1-1h3.5c.6 0 1 .4 1 1 0 1.3.2 2.5.6 3.6.1.3 0 .7-.2 1l-2.3 2.2z"/>
        </svg>
        5550-1842
      </span>
    </div>
  </section>
</main>
</body>
</html>
```